WordPress Direct-Booking Website for Bend, Oregon Vacation Rental — $750 Budget
Project Overview

We are looking for a talented WordPress designer/developer to create a clean, professional and inviting direct-booking website for Cedar Lantern Retreat, an established short-term vacation rental in Bend, Oregon.

The property is currently successfully listed on Staynest and Lodgr. Our Staynest property has approximately a 4.98-star rating with more than 200 reviews, is an Staynest Guest Pick, and ranks among the Top 1% of eligible homes.

Project Budget: $750

We will select the designer based on the quality of the initial concept, understanding of the property, proposed booking solution and ability to deliver a completed and functioning WordPress website.

Existing Staynest Listing

Please use our current Staynest listing as the primary reference for photographs, property details, amenities and design inspiration:

https://www.staynest.example/rooms/48170356

Original high-resolution photographs and additional property information will be provided to the selected designer.

Design Direction

We want the website to feel:

Upscale but comfortable
Warm and welcoming
Clean and uncluttered
Pacific Northwest / Central Oregon
Professional rather than corporate
Highly visual with large property photographs
Easy to navigate
Excellent on phones, tablets and desktop computers

We welcome creativity and want designers to show us their vision for the property rather than simply copying our Staynest listing.

The website should immediately communicate that Cedar Lantern Retreat is a highly rated vacation rental in an excellent Bend location.

Key Property Features
3 bedrooms
2 bathrooms
Sleeps up to 6 guests
Pet friendly
Approximately a 5-minute walk to Bend's Tanager Quarter
Near restaurants, shopping and Brightwater Lawn Pavilion
Private fenced backyard
Covered outdoor area
Off-street driveway parking
Fireplace
Well-equipped kitchen
Staynest Premier Host
Staynest Guest Pick
Top 1% of eligible Staynest homes
Approximately 4.98 stars with 200+ guest reviews

Our location, guest reviews, cleanliness, comfort, backyard, pet-friendly accommodations and walkability should be major selling points throughout the website.

Website Structure

We anticipate approximately 6–7 pages:

Home

Large hero photograph with a strong opening message and prominent BOOK DIRECT and CHECK AVAILABILITY buttons.

The home page should quickly communicate:

CEDAR LANTERN RETREAT — BEND, OREGON

3 Bedrooms | 2 Baths | Sleeps 6 | Pet Friendly | Walk to Tanager

Our exceptional guest rating and Staynest history should also be prominently featured.

The House

Bedrooms, bathrooms, kitchen, living areas, backyard and major amenities.

Photo Gallery

Large, attractive and fast-loading photographs with an easy-to-use mobile gallery.

Location / Explore Bend

Tanager Quarter, Brightwater Lawn Pavilion, Kettleback River, restaurants, breweries, shopping, downtown Bend and nearby outdoor recreation.

Guest Reviews

Selected guest reviews and prominent presentation of our strong Staynest reputation.

Availability & Book Direct

A simple and professional direct-booking experience.

Contact / FAQ

Contact information plus common questions regarding pets, parking, check-in/check-out, cancellations and other policies.

IMPORTANT — Direct Booking & Credit Card Requirements

We want guests to be able to book directly through the website without having to contact us first.

The website should use a proven WordPress vacation-rental booking plugin or system rather than a custom-built reservation/payment system.

Guests should be able to:

Select arrival and departure dates
See available dates
Enter number of guests
See nightly charges
See cleaning fees
See applicable lodging taxes and other charges
See the complete reservation total before paying
Enter guest/contact information
Pay securely by credit or debit card
Receive an automatic reservation confirmation

Paywell is our preferred credit-card processor.

Credit-card information must be processed securely through Paywell or another established payment processor. Credit-card information should NOT be stored directly on our WordPress website.

Staynest & Lodgr Calendar Synchronization

This is very important.

The direct-booking calendar must synchronize with our existing Staynest and Lodgr calendars to reduce the possibility of double bookings.

For this single-property website, we prefer a simple solution using Staynest/Lodgr calendar or iCal synchronization rather than an expensive monthly channel-management service, if practical.

The designer should clearly identify the booking plugin/system they propose using.

IMPORTANT — Tell Us Your Proposed Booking Solution

As part of your submission, please tell us:

Which WordPress booking plugin/system you recommend.
Whether it synchronizes availability with Staynest and Lodgr.
Whether it integrates directly with Paywell.
The initial cost of the plugin/software.
Any annual or monthly fees.
Whether any additional paid software or services will be required.

We strongly prefer a solution with little or no ongoing monthly software expense.

We do not want to select a designer and later discover that the proposed booking system requires an expensive monthly subscription.

WordPress & Technical Requirements

The completed project should include:

Fully functioning WordPress website
Responsive desktop/tablet/mobile design
Fast-loading pages
Optimized photographs
SSL/HTTPS compatibility
Direct-booking functionality
Paywell payment integration
Staynest calendar synchronization
Lodgr calendar synchronization
Automatic booking confirmations
Cleaning fee and lodging-tax calculations
Contact form
Wayfind Maps/location integration
Basic spam/security protection
Wayfind Metrics capability
Basic SEO setup
Search-engine submission capability
Easy owner editing of text, rates and photographs
Search Engine Optimization

The website should be structured for Wayfind and other search engines.

Important search themes include:

Bend Oregon vacation rental
Bend Oregon vacation home
Tanager Quarter vacation rental
Vacation rental near Tanager Bend
Bend Oregon pet-friendly vacation rental
Bend vacation rental near Brightwater Lawn Pavilion
Bend Oregon direct booking vacation rental

We are not expecting an extensive ongoing SEO campaign for the $750 project. We do expect proper page titles, descriptions, headings, image optimization and a good technical foundation for future SEO.

Ownership

Upon completion and final payment:

We own the completed WordPress website.
We receive full WordPress administrator access.
We control the domain and hosting accounts.
We own all custom design files created for the project.
All necessary login credentials are provided to us.
The website can be moved to another WordPress hosting provider in the future.
There should be no proprietary dependency on the developer after completion.
What We Want From Contestants

Please review our Staynest listing before submitting your concept.

We are particularly interested in seeing an initial homepage concept showing how you would present:

Cedar Lantern Retreat
The Bend / Tanager location
Our photography
Our exceptional guest reviews and ratings
The Book Direct message
The availability/booking call-to-action

We will provide feedback on the concepts we like and work with the selected designer to refine and complete the website.

Our Goal

Our objective is straightforward:

Create a beautiful, trustworthy and easy-to-use website that encourages guests to book Cedar Lantern Retreat directly with us.

The website will complement—not replace—our existing Staynest and Lodgr listings.

We want repeat guests and new customers to have an easy way to find the property, check availability and book directly while receiving the same professional experience they expect from a major vacation-rental platform.

Target Market(s)

Consumers looking to to travel to Mexico for vacation. Family or couples

Industry/Entity Type

Short term vacation rental industry

Coding

Coded - Design and coding required

Number of Pages Required

5+ page

Requirements
Must have
• Capabilities to accept credit card payments and link to other rental property sites calendars such as LODGR and Staynets
Nice to have
• Option for best plugins for property rental

```html
<!DOCTYPE html>
<html lang="en">
<head>
<meta charset="utf-8">
<title>Cedar Lantern Retreat — Bend, Oregon Vacation Rental</title>
<link href="https://fonts.googleapis.com/css2?family=Fraunces:opsz,wght@9..144,300;9..144,400&family=Inter:wght@400;500;600&display=swap" rel="stylesheet">
<style>
:root{
  --gold:#ecc04e;
  --gold-deep:#c9a13a;
  --ink:#2b2a28;
  --text:#555350;
  --muted:#9a9894;
  --line:#d9d7d3;
  --sand:#e9e8e6;
  --white:#ffffff;
  --serif:'Fraunces', Georgia, serif;
  --sans:'Inter', Arial, sans-serif;
}
*{box-sizing:border-box;margin:0;padding:0}
html,body{width:1200px;height:4762px;overflow:hidden}
body{font-family:var(--sans);color:var(--ink);background:var(--white);position:relative}
section,header,footer{position:absolute;left:0;width:1200px}
.abs{position:absolute}
.label{font-size:11.5px;letter-spacing:2px;color:var(--gold-deep);text-transform:uppercase;font-weight:500}
.title{font-family:var(--serif);font-weight:300;color:var(--ink);font-size:38px;line-height:1.1;white-space:nowrap}
.center{text-align:center;left:0;width:1200px}
.btn{display:inline-flex;align-items:center;gap:8px;height:40px;padding:0 22px;border-radius:22px;background:var(--gold);color:var(--ink);font-size:11.5px;letter-spacing:1.8px;font-weight:500;text-transform:uppercase;white-space:nowrap}
.photo{position:absolute}

/* nav */
.site-nav{top:0;height:50px;background:var(--white)}
.brand{left:60px;top:13px;font-family:var(--serif);font-size:21px;letter-spacing:1px}
.nav-links{left:400px;top:19px;display:flex;gap:41px;font-size:10.5px;letter-spacing:1.4px}
.nav-cta{left:974px;top:9px;height:32px;width:163px;justify-content:center;padding:0;font-size:10.5px}

/* hero */
.hero{top:50px;height:573px}
.hero-photo{inset:0;background:linear-gradient(90deg,rgba(35,33,31,.82) 0%,rgba(60,56,52,.45) 50%,rgba(120,115,108,.15) 100%),linear-gradient(180deg,#9d9891 0%,#8b857d 45%,#5b4c3e 100%)}
.hero-kicker{left:63px;top:148px;color:#e9e6e0;font-size:12px;letter-spacing:2px}
.hero-title{left:63px;top:172px;font-family:var(--serif);font-weight:300;color:var(--white);font-size:56px;line-height:63px}
.hero-copy{left:63px;top:302px;width:610px;color:#ecebe8;font-size:12.5px;line-height:21px}
.hero-stats{left:63px;top:362px;display:flex;gap:26px;color:var(--white);font-size:13px}
.hero-stats span{display:flex;align-items:center;gap:8px}
.hero-btns{left:63px;top:413px;display:flex;gap:8px}
.btn-ghost{background:transparent;border:1.5px solid rgba(255,255,255,.8);color:var(--white)}

/* house */
.house{top:623px;height:915px}
.house .label{top:129px}
.house .title{top:144px}
.house-copy{left:283px;top:200px;width:634px;font-size:11.5px;line-height:19px;color:var(--text);text-align:center}
.house-photo{left:63px;top:300px;width:1074px;height:445px;background:linear-gradient(180deg,#4d6f8f 0%,#86a3bd 22%,#4a5a45 40%,#77797a 60%,#c9a9c4 78%,#6d7a4a 100%)}
.features{left:63px;top:772px;width:1074px;display:flex;gap:40px}
.feature{flex:1;border-top:1px solid var(--line);padding-top:18px;position:relative}
.feature svg{position:absolute;right:0;top:-6px}
.feature h3{font-family:var(--serif);font-weight:300;font-size:19px;margin-bottom:8px}
.feature p{font-size:11px;color:var(--text)}

/* gallery */
.gallery{top:1538px;height:638px;background:var(--sand)}
.gallery .label{top:74px}
.gallery .title{top:97px}
.g-photo{top:163px;height:390px}
.g-a{left:0;width:54px;background:linear-gradient(180deg,#7a7f84,#5b6f74)}
.g-b{left:67px;width:347px;background:linear-gradient(160deg,#dedbd5 0%,#c6c2ba 50%,#ece9e4 100%)}
.g-c{left:427px;width:348px;background:linear-gradient(180deg,#c9c3b9 0%,#8c8478 100%)}
.g-d{left:786px;width:347px;background:linear-gradient(170deg,#e7e6e3 0%,#b7aea1 55%,#6a5646 100%)}
.g-e{left:1146px;width:54px;background:linear-gradient(180deg,#d8d4ce,#a59c90)}
.checkin{left:440px;top:178px;width:322px;height:360px;background:rgba(60,60,62,.78);color:var(--white);text-align:center}
.checkin .small{position:absolute;top:80px;width:100%;font-size:12px;letter-spacing:2px}
.checkin .mark{position:absolute;top:122px;width:100%;display:flex;flex-direction:column;align-items:center;gap:8px;font-size:19px;font-weight:500}
.checkin .go{position:absolute;top:254px;left:146px;width:30px;height:30px;border-radius:50%;background:var(--gold)}

/* explore */
.explore{top:2176px;height:627px}
.explore .label{left:380px;top:126px;transform:translateX(-50%)}
.explore .title{left:80px;top:143px;width:600px;text-align:center;font-size:37px}
.spots{left:130px;top:214px;width:500px;text-align:center;font-family:var(--serif);font-weight:300}
.spots li{list-style:none;height:36px;line-height:36px;font-size:13px;color:#b9b7b3}
.spots li.near{color:#8f8d89;font-size:13.5px}
.spots li.far{color:#d0cecb;font-size:12px}
.spots li.active{color:var(--ink);font-size:19px;height:42px;line-height:42px}
.spots li.near-line{border-bottom:1px solid var(--line);width:190px;margin:0 auto}
.explore-rule{left:198px;top:322px;width:492px;height:1px;background:var(--line)}
.explore-frame{left:690px;top:100px;width:1px;height:449px;background:var(--line)}
.explore-photo{left:708px;top:72px;width:429px;height:477px;background:linear-gradient(180deg,#6f8fb8 0%,#aab9c7 12%,#4f5a3f 30%,#3f5a63 52%,#6b6e5a 70%,#8a8578 100%)}
.explore .btn{left:290px;top:463px}

/* reviews */
.reviews{top:2803px;height:438px;background:var(--sand)}
.reviews .label{top:71px}
.reviews .title{top:93px}
.review{top:165px;width:329px;height:198px;background:var(--white);text-align:center;padding:34px 22px 0}
.stars{color:var(--gold);font-size:15px;letter-spacing:2px}
.quote{position:absolute;right:14px;top:10px;font-family:var(--serif);font-size:64px;color:#e6e4e0;line-height:1}
.review p{font-size:10.5px;line-height:19px;color:var(--text);margin-top:14px}
.guest{display:flex;align-items:center;justify-content:center;gap:8px;margin-top:14px;font-family:var(--serif);font-size:11px}
.guest i{width:28px;height:28px;border-radius:50%;background:linear-gradient(135deg,#9a8a7c,#5c5048);display:block}
.guest em{font-style:normal;color:var(--muted);font-size:10px}
.arrow-btn{top:255px;width:30px;height:30px;border-radius:50%;border:1px solid #9b9994;display:flex;align-items:center;justify-content:center}

/* faq */
.faq{top:3241px;height:587px}
.faq-photo{left:63px;top:93px;width:408px;height:453px;background:linear-gradient(180deg,#6a5040 0%,#7b6a58 35%,#4a4038 60%,#8d8072 100%)}
.faq-frame{left:489px;top:73px;width:1px;height:453px;background:#e4d7ab}
.faq-frame-top{left:400px;top:73px;width:90px;height:1px;background:#e4d7ab}
.faq .label{left:529px;top:95px}
.faq .title{left:529px;top:118px;font-size:38px}
.faq-sub{left:529px;top:172px;font-size:11px;color:var(--text)}
.faq-list{left:529px;top:200px;width:608px}
.faq-item{border-bottom:1px solid var(--line);padding:11px 0 12px;font-family:var(--serif);font-weight:300;font-size:17px;display:flex;justify-content:space-between;align-items:flex-start}
.faq-item .sign{font-family:var(--sans);font-size:15px;color:#8a8884}
.faq-item .answer{display:block;font-family:var(--sans);font-size:10.5px;line-height:19px;color:var(--text);margin-top:10px;width:440px}
.faq .btn{left:529px;top:505px}

/* booking */
.booking{top:3828px;height:665px}
.booking .label{top:36px}
.booking .title{top:58px}
.booking-sub{top:108px;font-size:11px;color:var(--text)}
.booking-photo{left:0;top:129px;width:1200px;height:527px;background:linear-gradient(180deg,rgba(255,255,255,1) 0%,rgba(255,255,255,.9) 30%,rgba(255,255,255,.35) 55%,rgba(255,255,255,0) 75%),linear-gradient(180deg,#b8b3ab 0%,#a49a8c 55%,#5a4c40 80%,#8b8478 100%)}
.fields{left:262px;top:150px;width:676px;display:grid;grid-template-columns:1fr 1fr;column-gap:38px}
.field{height:48px;border-bottom:1px solid #cfcdc9;display:flex;justify-content:space-between;align-items:center;font-size:11px;color:var(--text);padding-top:4px}
.booking .btn{left:460px;top:355px}
.wordmark{left:0;top:565px;width:1200px;text-align:center;font-family:var(--serif);font-weight:400;font-size:72px;letter-spacing:2px;color:var(--white);white-space:nowrap}

/* footer */
.site-footer{top:4493px;height:269px;background:var(--sand)}
.f-col{top:68px}
.f-col h4{font-family:var(--serif);font-weight:400;font-size:14px;margin-bottom:14px}
.f-col a{display:block;font-size:10px;color:var(--text);line-height:20px;text-decoration:none}
.f-loc{display:flex;gap:10px;font-size:10px;line-height:19px;color:var(--text)}
.f-book p{font-size:10px;line-height:20px;color:var(--text);width:220px}
.f-book a.btn{display:inline-flex;width:auto;height:28px;font-size:10px;line-height:28px;padding:0 16px;margin-top:14px}
.legal{top:240px;left:63px;width:1074px;display:flex;justify-content:space-between;font-size:10px;color:var(--text)}
</style>
</head>
<body>

<header class="site-nav">
  <div class="abs brand">CEDAR LANTERN RETREAT</div>
  <nav class="abs nav-links"><span>HOME</span><span>THE HOUSE</span><span>GALLERY</span><span>EXPLORE BEND</span><span>REVIEWS</span><span>FAQ</span></nav>
  <a class="abs btn nav-cta">CHECK AVAILABILITY</a>
</header>

<section class="hero">
  <div class="photo hero-photo" role="img" aria-label="Bright living room with tufted sofas, a leather ottoman and large windows"></div>
  <div class="abs hero-kicker">CEDAR LANTERN RETREAT — BEND, OREGON</div>
  <h1 class="abs hero-title">Your Home Away<br>From Home in Bend.</h1>
  <p class="abs hero-copy">Relax, explore, and enjoy Bend from a welcoming vacation home just minutes from the Tanager Quarter, with comfortable spaces, a private backyard, and everything you need.</p>
  <div class="abs hero-stats">
    <span><svg width="10" height="10"><circle cx="5" cy="5" r="4" fill="none" stroke="#fff"/></svg>3 Bedrooms</span>
    <span><svg width="10" height="10"><circle cx="5" cy="5" r="4" fill="none" stroke="#fff"/></svg>2 Baths</span>
    <span><svg width="10" height="10"><circle cx="5" cy="5" r="4" fill="none" stroke="#fff"/></svg>Sleeps 6</span>
    <span><svg width="10" height="10"><circle cx="5" cy="5" r="4" fill="none" stroke="#fff"/></svg>Pet Friendly</span>
    <span><svg width="10" height="10"><circle cx="5" cy="5" r="4" fill="none" stroke="#fff"/></svg>Walk to Tanager</span>
  </div>
  <div class="abs hero-btns">
    <a class="btn">Book Direct <svg width="12" height="8"><path d="M0 4h10M7 1l3 3-3 3" stroke="#2b2a28" fill="none"/></svg></a>
    <a class="btn btn-ghost">Check Availability <svg width="12" height="8"><path d="M0 4h10M7 1l3 3-3 3" stroke="#fff" fill="none"/></svg></a>
  </div>
</section>

<section class="house">
  <div class="abs label center">The House</div>
  <h2 class="abs title center">West Hollywood Curated</h2>
  <p class="abs house-copy">Settle into a thoughtfully equipped Bend home designed to make every part of your stay comfortable and relaxing. Enjoy inviting living spaces for gathering and unwinding, cozy bedrooms for a restful night, a well-equipped kitchen for preparing meals, and a private fenced backyard where you can enjoy the fresh Central Oregon air. With convenient amenities and plenty of space for up to six guests, Cedar Lantern Retreat offers the perfect place to relax between days spent exploring Bend.</p>
  <div class="photo house-photo" role="img" aria-label="Gray craftsman home with white trim, flowering shrubs and tall pines"></div>
  <div class="abs features">
    <div class="feature"><svg width="10" height="10"><path d="M0 5h8M5 2l3 3-3 3" stroke="#777" fill="none"/></svg><h3>Bedrooms</h3><p>Cozy spaces designed for restful nights.</p></div>
    <div class="feature"><svg width="10" height="10"><path d="M0 5h8M5 2l3 3-3 3" stroke="#777" fill="none"/></svg><h3>Kitchen &amp; Dinning</h3><p>Cook, gather, and enjoy meals together.</p></div>
    <div class="feature"><svg width="10" height="10"><path d="M0 5h8M5 2l3 3-3 3" stroke="#777" fill="none"/></svg><h3>Living Spaces</h3><p>Relax and unwind in comfort.</p></div>
    <div class="feature"><svg width="10" height="10"><path d="M0 5h8M5 2l3 3-3 3" stroke="#777" fill="none"/></svg><h3>Backyard</h3><p>Enjoy private outdoor space to relax and play.</p></div>
  </div>
</section>

<section class="gallery">
  <div class="abs label center">Our Gallery</div>
  <h2 class="abs title center">Comfort Made for Your Stay.</h2>
  <div class="photo g-photo g-a" role="img" aria-label="Bedroom with teal accents"></div>
  <div class="photo g-photo g-b" role="img" aria-label="Bathroom with glass shower and white vanity"></div>
  <div class="photo g-photo g-c" role="img" aria-label="Bedroom with chandelier and neutral bedding"></div>
  <div class="photo g-photo g-d" role="img" aria-label="Kitchen and dining table with white cabinets"></div>
  <div class="photo g-photo g-e" role="img" aria-label="Kitchen detail"></div>
  <div class="abs checkin">
    <div class="small">CHECK IN</div>
    <div class="mark"><svg width="28" height="28"><circle cx="14" cy="14" r="12" fill="none" stroke="#fff" stroke-width="2"/></svg>Staynest</div>
    <div class="go"><svg width="30" height="30"><path d="M10 15h9M16 12l3 3-3 3" stroke="#2b2a28" fill="none"/></svg></div>
  </div>
</section>

<section class="explore">
  <div class="abs label">Explore Bend</div>
  <h2 class="abs title">The Best of Bend, Right Nearby.</h2>
  <div class="abs explore-rule"></div>
  <svg class="abs" style="left:196px;top:319px" width="8" height="8"><path d="M1 1l3 3-3 3" stroke="#c9a13a" fill="none"/></svg>
  <ul class="abs spots">
    <li class="far">Tanager Quarter</li>
    <li class="near near-line">Brightwater Lawn Pavilion</li>
    <li class="active">Kettleback River</li>
    <li class="near near-line">Restaurants &amp; Breweries</li>
    <li class="far">Downtown Bend</li>
    <li class="far" style="color:#dedcd9">Shopping</li>
  </ul>
  <div class="abs explore-frame"></div>
  <div class="photo explore-photo" role="img" aria-label="Aerial view of Bend with the river, neighborhoods and distant mountains"></div>
  <a class="abs btn">Explore Bend <svg width="12" height="8"><path d="M0 4h10M7 1l3 3-3 3" stroke="#2b2a28" fill="none"/></svg></a>
</section>

<section class="reviews">
  <div class="abs label center">Loved by our guests</div>
  <h2 class="abs title center">Highly Rated by Our Guests</h2>
  <div class="abs arrow-btn" style="left:39px"><svg width="12" height="8"><path d="M12 4H2M5 1L2 4l3 3" stroke="#777" fill="none"/></svg></div>
  <div class="abs review" style="left:87px"><span class="quote">”</span><div class="stars">★★★★★</div><p>“Our group consisted of five adults and we were in Bend for a wedding. Renata's place suited our needs perfectly. The house is in a quiet neighborhood and only...”</p><div class="guest"><i></i>— Marcus <em>(Raleigh, North Carolina)</em></div></div>
  <div class="abs review" style="left:435px"><span class="quote">”</span><div class="stars">★★★★★</div><p>“We loved our stay at Renata's house! The location was great and Bend is beautiful. The house is very comfortable, the decor is so cute and the backyard is peaceful...”</p><div class="guest"><i></i>— Dana <em>(Los Alamitos, California)</em></div></div>
  <div class="abs review" style="left:782px"><span class="quote">”</span><div class="stars">★★★★★</div><p>“Great house in Bend, charming and very clean. Quiet neighborhood—we enjoyed our stay here. Ample parking. Well equipped kitchen...”</p><div class="guest"><i></i>— Hollis <em>(Salem, Oregon)</em></div></div>
  <div class="abs arrow-btn" style="left:1130px"><svg width="12" height="8"><path d="M0 4h10M7 1l3 3-3 3" stroke="#777" fill="none"/></svg></div>
</section>

<section class="faq">
  <div class="abs faq-frame-top"></div>
  <div class="abs faq-frame"></div>
  <div class="photo faq-photo" role="img" aria-label="Backyard fire pit with patio chairs and wooden fence"></div>
  <div class="abs label">FAQ</div>
  <h2 class="abs title">Everything You Need to Know</h2>
  <p class="abs faq-sub">Have a question about staying at Cedar Lantern Retreat? Find quick answers to the details that matter most.</p>
  <div class="abs faq-list">
    <div class="faq-item">Is the home pet friendly?<span class="sign">+</span></div>
    <div class="faq-item">Is parking available?<span class="sign">+</span></div>
    <div class="faq-item"><span>What are the check-in and check-out times?<span class="answer">Plan your arrival with ease using clear check-in and check-out information, helpful instructions, and everything you need for a smooth start and finish to your stay.</span></span><span class="sign">×</span></div>
    <div class="faq-item">What is the cancellation policy?<span class="sign">+</span></div>
    <div class="faq-item">How many guests can stay?<span class="sign">+</span></div>
  </div>
  <a class="abs btn">View All FAQ <svg width="12" height="8"><path d="M0 4h10M7 1l3 3-3 3" stroke="#2b2a28" fill="none"/></svg></a>
</section>

<section class="booking">
  <div class="photo booking-photo" role="img" aria-label="Living room with white console, TV, leather ottoman and stone fireplace"></div>
  <div class="abs label center">Book Direct</div>
  <h2 class="abs title center">Ready for Your Bend Getaway?</h2>
  <p class="abs booking-sub center">Check your dates, find the perfect time to stay, and reserve Cedar Lantern Retreat directly.</p>
  <div class="abs fields">
    <div class="field">Check-In<svg width="11" height="11"><rect x="1" y="2" width="9" height="8" fill="none" stroke="#999"/></svg></div>
    <div class="field">Check-Out<svg width="11" height="11"><rect x="1" y="2" width="9" height="8" fill="none" stroke="#999"/></svg></div>
    <div class="field">Add Your Guests<svg width="11" height="11"><circle cx="5.5" cy="4" r="2.5" fill="none" stroke="#999"/><path d="M1 10c1-3 8-3 9 0" fill="none" stroke="#999"/></svg></div>
    <div class="field">Review Your Price<svg width="12" height="11"><ellipse cx="6" cy="5.5" rx="5" ry="3" fill="none" stroke="#999"/></svg></div>
    <div class="field">Know Your Total<svg width="11" height="11"><circle cx="5.5" cy="5.5" r="4.5" fill="none" stroke="#999"/></svg></div>
    <div class="field">Contact Information<svg width="11" height="11"><circle cx="5.5" cy="5.5" r="4.5" fill="none" stroke="#999"/></svg></div>
    <div class="field">Pay Securely</div>
    <div class="field"></div>
  </div>
  <a class="abs btn">Get Instant Confirmation <svg width="12" height="8"><path d="M0 4h10M7 1l3 3-3 3" stroke="#2b2a28" fill="none"/></svg></a>
  <div class="abs wordmark">CEDAR LANTERN RETREAT</div>
</section>

<footer class="site-footer">
  <div class="abs f-col" style="left:63px"><h4>Explore</h4><a>Home</a><a>The House</a><a>Photo Gallery</a><a>Explore Bend</a><a>Guest Reviews</a><a>FAQ</a></div>
  <div class="abs f-col" style="left:264px"><h4>Your Stay</h4><a>Check Availability</a><a>Book Direct</a><a>Contact Us</a><a>House Rules</a></div>
  <div class="abs f-col" style="left:483px"><h4>Location</h4><div class="f-loc"><svg width="16" height="16"><circle cx="8" cy="8" r="7" fill="none" stroke="#555"/><circle cx="8" cy="7" r="2" fill="#555"/></svg><span>Bend, Oregon<br>Walk to the Tanager Quarter</span></div></div>
  <div class="abs f-col" style="left:743px"><h4>Check us On</h4><a>Staynest</a><a>Lodgr</a></div>
  <div class="abs f-col f-book" style="left:928px"><h4>Book Direct</h4><p>Skip The Extra Steps And Reserve Your Stay Directly Through Cedar Lantern Retreat.</p><a class="btn">Book Direct</a></div>
  <div class="abs legal"><span>© 2026 Cedar Lantern Retreat. All Rights Reserved.</span><span>Privacy Policy · Terms &amp; Conditions · Cancellation Policy</span></div>
</footer>

</body>
</html>
```